Broadway Haulage website

We need a website design for a towing company based in Australia.
The design should be simple and minimalist. The site can be in colours of the logo are Blue, Red and White (see attached) - but we'd like to see options in some sort of industrial looking metallic theme if possible.
We base our business on our friendly and efficient customer service, the design should attempt to convey this in some way.

Industry/Entity Type

Industrial

Font styles to use
Sans Serif

```html
<!DOCTYPE html>
<html lang="en">
<head>
<meta charset="utf-8">
<title>Broadway Haulage</title>
<link href="https://fonts.googleapis.com/css2?family=Arimo:wght@400;700&family=Titillium+Web:wght@400;600&display=swap" rel="stylesheet">
<style>
:root{
  --blue:#0a3d8f;
  --blue-dark:#072e6e;
  --red:#b50d12;
  --grey-bg:#e6e6e6;
  --text:#333;
  --muted:#555;
  --footer:#4b4b4b;
  --white:#fff;
}
*{margin:0;padding:0;box-sizing:border-box}
html,body{width:890px;height:1200px;overflow:hidden;background:var(--white);font-family:"Arimo",Arial,sans-serif;color:var(--text)}
.page{position:relative;width:890px;height:1200px}
.abs{position:absolute}
.topline{top:21px;font-size:10.5px;color:#222}
.topline.left{left:73px}
.topline.right{right:73px;display:flex;align-items:center;gap:8px}
.nav{top:51px;left:0;width:890px;height:38px;background:linear-gradient(#0d47a1,var(--blue-dark));border-bottom:2px solid #d8d8d8}
.nav a{position:absolute;top:0;height:38px;line-height:38px;color:var(--white);font-size:11px;text-decoration:none;letter-spacing:.3px;padding:0 10px;border-right:1px solid rgba(0,0,0,.25)}
.brand{z-index:5;left:392px;top:14px;width:106px;height:112px;background:var(--white);border-radius:8px;display:flex;flex-direction:column;align-items:center;justify-content:center;gap:8px;box-shadow:0 1px 4px rgba(0,0,0,.2)}
.brand .mark{width:28px;height:28px;background:var(--blue)}
.brand span{font-family:"Titillium Web",sans-serif;font-weight:600;font-size:13px;color:var(--blue);text-align:center;line-height:1.15}
.stage{top:91px;left:0;width:890px;height:365px;background:radial-gradient(ellipse at center,#fafafa 40%,var(--grey-bg))}
.slider{top:142px;left:74px;width:742px;height:282px;background:#fff;padding:3px;box-shadow:0 0 3px rgba(0,0,0,.2)}
.slide{width:100%;height:100%;background:linear-gradient(120deg,#3b3b3b 0%,#5a6a4a 35%,#b9bcbf 60%,#7a8460 100%)}
.caption{top:275px;left:130px;width:336px;height:45px;background:rgba(255,255,255,.3);font-family:"Titillium Web",sans-serif;font-size:26px;color:var(--white);line-height:45px;padding-left:10px}
.arrow{top:285px;width:20px;height:24px;background:rgba(255,255,255,.6);display:flex;align-items:center;justify-content:center}
.dots{top:402px;left:398px;width:92px;height:20px;background:#ddd;border-radius:5px 5px 0 0;display:flex;align-items:center;justify-content:center;gap:5px}
.dots i{width:8px;height:8px;border-radius:50%;background:#888}
.dots i.on{background:var(--red)}
.quick{top:456px;left:0;width:890px;height:71px;background:var(--blue)}
.field{top:474px;width:140px;height:31px;background:linear-gradient(#fff,#e9e9e9);border-radius:2px;font-size:9px;color:#555;padding-left:15px;line-height:31px}
.quick-btn{top:474px;left:703px;width:110px;height:31px;background:var(--red);color:var(--white);font-family:"Titillium Web",sans-serif;font-size:14px;text-align:center;line-height:31px}
.photo{display:block}
h2,h3,.head{font-family:"Titillium Web",sans-serif;font-weight:400}
.welcome-h{top:551px;left:264px;font-size:14px}
.body{font-size:8.5px;line-height:17.8px;color:var(--muted);text-align:justify}
.learn{top:752px;left:470px;font-size:8.5px;color:var(--red)}
.updates{top:544px;left:572px;width:244px;height:220px;background:#f4f4f4;box-shadow:0 1px 3px rgba(0,0,0,.2)}
.updates .bar{height:34px;background:var(--blue);color:var(--white);font-family:"Titillium Web",sans-serif;font-size:13px;line-height:34px;padding-left:14px;position:relative}
.updates .bar em{position:absolute;right:14px;font-style:normal;font-size:10px}
.upd{position:absolute;left:10px;width:225px}
.upd .thumb{position:absolute;left:0;top:0;width:74px;height:64px}
.upd .txt{position:absolute;left:86px;top:0;width:140px}
.upd h4{font-weight:400;font-size:10px;color:#222;margin-bottom:4px}
.upd .date{font-size:8.5px;color:#444;margin-bottom:4px}
.upd p{font-size:8.5px;line-height:16px;color:#555;text-align:justify}
.services-h{top:791px;left:73px;font-size:13px}
.card{top:819px;width:236px;height:287px;background:linear-gradient(#fff 60%,#f2f2f2);box-shadow:0 0 3px rgba(0,0,0,.15)}
.card .pic{position:absolute;top:3px;left:2px;width:232px;height:134px}
.card h3{position:absolute;top:148px;left:14px;font-size:15px;color:#222}
.card p{position:absolute;top:177px;left:14px;width:208px;font-size:8.5px;line-height:16.3px;color:#444;text-align:justify}
.card .btn{position:absolute;top:250px;left:15px;width:61px;height:24px;background:var(--red);color:var(--white);font-size:10px;text-align:center;line-height:24px}
.footer{top:1133px;left:0;width:890px;height:67px;background:var(--footer);color:#eee}
.footer .links{position:absolute;top:15px;left:75px;font-size:8.5px}
.footer .copy{position:absolute;top:43px;left:75px;font-size:8.5px}
.social{position:absolute;top:21px;left:655px;display:flex;gap:10px}
.social i{width:24px;height:24px;border-radius:50%;background:linear-gradient(#eee,#aaa)}
</style>
</head>
<body>
<div class="page">
  <div class="abs topline left">Country Callers 1800 472 910</div>
  <div class="abs topline right">
    <svg width="14" height="14" viewBox="0 0 24 24" aria-hidden="true"><path fill="#111" d="M6.6 10.8a15.1 15.1 0 006.6 6.6l2.2-2.2c.3-.3.7-.4 1-.2 1.1.4 2.3.6 3.6.6.6 0 1 .4 1 1V20c0 .6-.4 1-1 1A17 17 0 013 4c0-.6.4-1 1-1h3.5c.6 0 1 .4 1 1 0 1.3.2 2.5.6 3.6.1.3 0 .7-.2 1z"/></svg>
    <span>1(800) 555-0192</span>
  </div>

  <nav class="abs nav">
    <a style="left:73px;background:rgba(0,0,0,.12)">HOME</a>
    <a style="left:139px">ABOUT US</a>
    <a style="left:227px">TOWING SERVICES</a>
    <a style="left:539px;border-left:1px solid rgba(0,0,0,.25)">NEWS &amp; EVENTS</a>
    <a style="left:667px">BLOG</a>
    <a style="left:730px;border-right:0">CONTACT US</a>
  </nav>

  <div class="abs stage"></div>
  <div class="abs brand"><div class="mark"></div><span>Broadway<br>Haulage</span></div>

  <div class="abs slider"><div class="slide" role="img" aria-label="Tow truck carrying a silver pickup on its flatbed"></div></div>
  <div class="abs caption">Towing services in Australia</div>
  <div class="abs arrow" style="left:78px"><svg width="8" height="10" viewBox="0 0 8 10"><path d="M6 1L2 5l4 4" stroke="#fff" stroke-width="2" fill="none"/></svg></div>
  <div class="abs arrow" style="left:792px"><svg width="8" height="10" viewBox="0 0 8 10"><path d="M2 1l4 4-4 4" stroke="#fff" stroke-width="2" fill="none"/></svg></div>
  <div class="abs dots"><i></i><i></i><i class="on"></i><i></i><i></i><i></i></div>

  <div class="abs quick"></div>
  <div class="abs field" style="left:74px">Name</div>
  <div class="abs field" style="left:230px">Email</div>
  <div class="abs field" style="left:386px">Phone no</div>
  <div class="abs field" style="left:542px">Booking time</div>
  <div class="abs quick-btn">Quick contact</div>

  <div class="abs photo" style="top:554px;left:74px;width:173px;height:208px;background:linear-gradient(#4d6a3a,#9a9a9a 45%,#c8343a 80%)" role="img" aria-label="White SUV loaded on a red tow truck bed beside a highway"></div>
  <h2 class="abs welcome-h">Welcome To Broadway Haulage</h2>
  <div class="abs body" style="top:578px;left:264px;width:252px">Lorem ipsum dolor sit amet conse ctetur adipisicing elit, sed do eiusmod tempor incididunt ut labore et dolore magna aliqua. Ut enim ad minim veniam, quis nostrud exercitation ullamco laboris.Lorem ipsum dolor sit amet conse ctetur adipisicing elit, sed do eiusmod tempor incididunt ut labore et dolore magna aliqua. Ut enim ad minim veniam, quis nostrud exercitation ullamco laboris.</div>
  <div class="abs body" style="top:709px;left:264px;width:252px">Lorem ipsum dolor sit amet conse ctetur adipisicing elit, sed do eiusmod tempor incididunt ut labore et</div>
  <div class="abs learn">Learn More</div>

  <div class="abs updates">
    <div class="bar">Latest Updates<em>‹ &nbsp; ›</em></div>
    <div class="upd" style="top:48px">
      <div class="thumb" role="img" aria-label="White tow truck in a depot" style="background:linear-gradient(#aab4c0,#e8e8e8 60%,#777)"></div>
      <div class="txt"><h4>Towing Service our Moto</h4><div class="date">10/02/2014</div><p>Lorem ipsum dolor sit amet conse ctetur Lorem ipsum dolor sit amet conse cteturconse ctetur</p></div>
    </div>
    <div class="upd" style="top:142px">
      <div class="thumb" role="img" aria-label="Heavy recovery trucks parked in a row" style="background:linear-gradient(#b7c6d6,#eaeaea 55%,#8a8a7a)"></div>
      <div class="txt"><h4>Our Heavy Recovery trucks</h4><div class="date">10/02/2014</div><p>Lorem ipsum dolor sit amet conse ctetur Lorem ipsum dolor</p></div>
    </div>
  </div>

  <h2 class="abs services-h">Our Services</h2>

  <div class="abs card" style="left:74px">
    <div class="pic" role="img" aria-label="Flatbed tow truck carrying a silver SUV" style="background:linear-gradient(#9fb3c8,#4e6b3c 45%,#d9d9d9 65%,#777)"></div>
    <h3>Heavy Towing</h3>
    <p>Lorem ipsum dolor sit amet conse ctetur adipisicing elit, sed do eiusmod tempor incididunt ut labore et dolore magna aliqua. Ut enim ad minim veniam, quis nostrud exercitation ullamco</p>
    <div class="btn">More Info</div>
  </div>
  <div class="abs card" style="left:327px">
    <div class="pic" role="img" aria-label="White recovery truck carrying a red sports car" style="background:linear-gradient(#e0e0e0,#f5f5f5 35%,#c62828 55%,#aaa)"></div>
    <h3>Recovery Specialist</h3>
    <p>Lorem ipsum dolor sit amet conse ctetur adipisicing elit, sed do eiusmod tempor incididunt ut labore et dolore magna aliqua. Ut enim ad minim veniam, quis nostrud exercitation ullamco laboris</p>
    <div class="btn">More Info</div>
  </div>
  <div class="abs card" style="left:580px">
    <div class="pic" role="img" aria-label="Red tow truck loading a red classic car" style="background:linear-gradient(#5f7a48,#b71c1c 55%,#555)"></div>
    <h3>Semi-Tilts-Low Loaders</h3>
    <p>Lorem ipsum dolor sit amet conse ctetur adipisicing elit, sed do eiusmod tempor incididunt ut labore et dolore magna aliqua. Ut enim ad minim veniam, quis nostrud exercitation ullamco laboris</p>
    <div class="btn">More Info</div>
  </div>

  <footer class="abs footer">
    <div class="links">Home | Towing services &nbsp;| &nbsp;Features &nbsp;| &nbsp;About us &nbsp;| &nbsp;Login</div>
    <div class="copy">© 2014 Broadway Haulage. All rights reserved. Terms of Use</div>
    <div class="social"><i></i><i></i><i></i><i></i><i></i></div>
  </footer>
</div>
</body>
</html>
```